I want to revise my business card design and get a more modern and up to date design.

Brolvane Handyman Sevices originated from a family-owned and operated contractor business, performing home renovation, addition, and construction work in the NYC area since 2004. Today, we specialize in reliable and affordable handyman services for residential and commercial clients In 2014, we expanded to northern New Jersey. In 2016, we brought quality home improvement and repair services to new Bucks County, PA, and nearby New Jersey areas.
Target Market(s)
Home owners and business that might be looking for a General contractor, handyman, cleaning services and Home maintenance and property.
Industry/Entity Type
Construction Company
Contact Information for Business Card
I am open to new ideas
Colors
Designer to choose colors to be used in the design.
Look and feel
Each slider illustrates characteristics of the customer's brand and the style your logo design should communicate.

```html
<!DOCTYPE html>
<html lang="en">
<head>
<meta charset="utf-8">
<title>Brolvane Handyman Sevices – Business Card</title>
<link href="https://fonts.googleapis.com/css2?family=Lato:ital,wght@0,400;0,700;0,900;1,400&display=swap" rel="stylesheet">
<style>
  :root {
    --stage: #3a3a3a;
    --card: #1d1d1f;
    --card-back: #19191b;
    --red: #e3222b;
    --yellow: #f2c21b;
    --white: #ffffff;
    --soft: #d9d9d9;
    --rule: #5a5a5a;
  }
  * { margin: 0; padding: 0; box-sizing: border-box; }
  html, body { width: 1200px; height: 1108px; overflow: hidden; }
  body {
    background: var(--stage);
    font-family: "Lato", sans-serif;
    position: relative;
  }
  .card {
    position: absolute;
    top: 174px;
    width: 440px;
    height: 760px;
    border-radius: 22px;
    background: var(--card);
    color: var(--white);
    text-align: center;
    overflow: hidden;
  }
  .card--front { left: 120px; }
  .card--back { left: 640px; background: var(--card-back); }

  /* brand block */
  .brand { display: flex; align-items: center; justify-content: center; gap: 14px; }
  .brand__dot { width: 58px; height: 58px; border-radius: 50%; background: var(--red); flex: none; }
  .brand__name { font-weight: 900; font-size: 64px; letter-spacing: -1px; color: var(--white); line-height: 1; }
  .brand__sub { font-size: 14px; letter-spacing: 5px; color: var(--soft); margin-top: 8px; }

  .card--front .brand-wrap { margin-top: 112px; }
  .licensed { font-style: italic; color: var(--yellow); font-size: 20px; margin-top: 22px; }

  .person { margin-top: 92px; }
  .person__name { color: var(--red); font-size: 28px; letter-spacing: 0.5px; }
  .person__role { color: var(--yellow); font-size: 18px; margin-top: 2px; }

  .rule { width: 230px; height: 1px; background: var(--rule); margin: 18px auto; }

  .contact { font-size: 20px; line-height: 1.4; color: var(--white); }
  .services { font-size: 19px; line-height: 1.35; color: var(--white); }
  .tagline { margin-top: 22px; font-size: 21px; color: var(--yellow); }
  .tagline .sep { color: var(--red); margin: 0 6px; }

  /* back */
  .pattern {
    position: absolute; inset: 0 0 auto 0; height: 560px;
    background: linear-gradient(180deg, #26262a 0%, #1e1e21 70%, var(--card-back) 100%);
  }
  .back-content { position: absolute; left: 0; right: 0; top: 330px; }
  .back-content .brand__dot { width: 50px; height: 50px; margin: 0 auto 34px; }
  .back-content .brand__name { font-size: 80px; }
  .back-rule { width: 300px; height: 1px; background: var(--yellow); margin: 18px auto 0; opacity: 0.7; }
  .social { display: flex; justify-content: center; gap: 10px; margin-top: -14px; }
  .social span { width: 26px; height: 26px; border-radius: 50%; border: 2px solid var(--yellow); background: var(--card-back); }
  .hashtag { color: var(--yellow); font-size: 22px; margin-top: 12px; }
  .license { color: var(--white); font-size: 19px; margin-top: 12px; }
</style>
</head>
<body>

<section class="card card--front" aria-label="Business card front">
  <div class="brand-wrap">
    <div class="brand">
      <span class="brand__dot"></span>
      <span class="brand__name">Brolvane</span>
    </div>
    <p class="brand__sub">HANDYMAN SERVICES</p>
    <p class="licensed">Licensed and Insured</p>
  </div>

  <div class="person">
    <p class="person__name">TEODORO VASQUEZ</p>
    <p class="person__role">Owner</p>
  </div>
  <div class="rule"></div>
  <div class="contact">
    <p>(215) 555-0148</p>
    <p>brolvanehandyman@mail.com</p>
    <p>www.brolvane.com</p>
  </div>
  <div class="rule"></div>
  <div class="services">
    <p>General Contractor, Property Maintenance,</p>
    <p>Handyman and Cleaning Services.</p>
  </div>
  <p class="tagline">Repair<span class="sep">●</span>Improve<span class="sep">●</span>Maintain<span class="sep">●</span>Remodel</p>
</section>

<section class="card card--back" aria-label="Business card back">
  <div class="pattern" role="img" aria-label="Faint repeating brand pattern"></div>
  <div class="back-content">
    <span class="brand__dot" style="display:block"></span>
    <p class="brand__name">Brolvane</p>
    <p class="brand__sub">HANDYMAN SERVICES</p>
    <div class="back-rule"></div>
    <div class="social" aria-label="Social media">
      <span></span><span></span><span></span><span></span>
    </div>
    <p class="hashtag">#brolvanehandymanservices</p>
    <p class="license">PA 304518 and NJ 13VH07716420</p>
  </div>
</section>

</body>
</html>
```